Book cover for a book about how to support a friend in grief.

The title of the book is "Quiet Hands on Heavy Days: Standing Beside Someone Across Hard Seasons" by Daniel P. Hartwig. I am a grief counselor and am passionate about educating people on how to better support someone in grief. I'd like the cover to tell a story. Maybe a person in grief and a friend standing near who doesn't know what to say. The image should appeal to all genders. I am open to ANY other ideas for the cover. Grief is a heavy topic but I don't want the cover to feel sad. It should convey hope.

```html
<!DOCTYPE html>
<html lang="en">
<head>
<meta charset="utf-8">
<title>Quiet Hands on Heavy Days — Book Cover</title>
<link href="https://fonts.googleapis.com/css2?family=Baloo+2:wght@800&family=Caveat:wght@600&family=Arimo:wght@400;700&display=swap" rel="stylesheet">
<style>
  :root {
    --night: #25272c;
    --wall-light: #d3d5d2;
    --mustard: #c98e1f;
    --teal: #1d8c9c;
    --white: #ffffff;
    --ink: #1b1b1b;
    --soft-grey: #e6e6e6;
  }
  * { margin: 0; padding: 0; box-sizing: border-box; }
  html, body { width: 982px; height: 1200px; overflow: hidden; background: #ffffff; }
  .cover { position: relative; width: 982px; height: 1200px; overflow: hidden; background: var(--wall-light); }
  .cover-art { position: absolute; inset: 0; }
  .title { position: absolute; left: 0; top: 0; width: 100%; font-family: "Baloo 2", sans-serif; text-transform: uppercase; line-height: 0.9; font-weight: 800; }
  .title-lead { position: absolute; left: 112px; top: 16px; font-size: 230px; color: var(--mustard); letter-spacing: 12px; }
  .title-middle { position: absolute; left: 152px; top: 232px; display: flex; align-items: center; gap: 16px; }
  .title-middle .white { font-size: 90px; color: var(--white); }
  .title-middle .stack { font-size: 48px; color: var(--teal); line-height: 0.92; }
  .title-tail { position: absolute; left: 152px; top: 332px; font-size: 92px; color: var(--mustard); letter-spacing: 2px; }
  .subtitle { position: absolute; left: 200px; top: 425px; font-family: "Caveat", cursive; font-size: 38px; color: var(--white); }
  .bubble { position: absolute; }
  .author { position: absolute; left: 0; width: 100%; top: 1090px; text-align: center; font-family: "Arimo", sans-serif; }
  .author-name { font-size: 46px; font-weight: 700; color: var(--white); letter-spacing: -0.5px; }
  .author-role { font-size: 22px; color: var(--soft-grey); letter-spacing: 3px; margin-top: 2px; }
</style>
</head>
<body>
<main class="cover">
  <svg class="cover-art" width="982" height="1200" viewBox="0 0 982 1200">
    <defs>
      <linearGradient id="wall" x1="0" y1="0" x2="0" y2="1">
        <stop offset="0" stop-color="#cfd1ce"/>
        <stop offset="1" stop-color="#c2c4c1"/>
      </linearGradient>
      <linearGradient id="water" x1="0" y1="0" x2="0" y2="1">
        <stop offset="0" stop-color="#23252a"/>
        <stop offset="0.7" stop-color="#2c2d33"/>
        <stop offset="1" stop-color="#4a3a45"/>
      </linearGradient>
      <linearGradient id="griever" x1="0" y1="0" x2="0" y2="1">
        <stop offset="0" stop-color="#3b2c27"/>
        <stop offset="0.3" stop-color="#9a8288"/>
        <stop offset="0.6" stop-color="#a68f96"/>
        <stop offset="0.8" stop-color="#4f6f98"/>
        <stop offset="1" stop-color="#3d5a80"/>
      </linearGradient>
      <linearGradient id="friend" x1="0" y1="0" x2="0" y2="1">
        <stop offset="0" stop-color="#2f221c"/>
        <stop offset="0.3" stop-color="#7fa9c2"/>
        <stop offset="0.65" stop-color="#8db6cd"/>
        <stop offset="1" stop-color="#6f9dbb"/>
      </linearGradient>
    </defs>
    <rect width="982" height="1200" fill="url(#wall)"/>
    <path d="M0 0 H982 V280 C880 300 800 360 770 470 C720 650 510 900 482 1200 C462 950 430 690 365 580 C320 510 150 472 0 462 Z" fill="url(#water)" role="img" aria-label="Dark rippling water texture"/>
    <path class="figure-griever" d="M30 1200 V880 C30 790 110 733 220 733 C330 733 415 790 415 880 V1200 Z" fill="url(#griever)" opacity="0.9" role="img" aria-label="Photo of a young person in a mauve hoodie sitting against the wall, hugging their knees and looking away in grief"/>
    <path class="figure-friend" d="M520 1200 V840 C520 750 610 689 722 689 C834 689 925 750 925 840 V1200 Z" fill="url(#friend)" opacity="0.9" role="img" aria-label="Photo of a friend in a blue knit sweater sitting nearby, hugging their knees, unsure what to say"/>
  </svg>

  <svg class="bubble bubble-heart" style="left:60px;top:490px" width="262" height="210" viewBox="0 0 262 210">
    <g fill="#ffffff">
      <circle cx="70" cy="80" r="52"/><circle cx="130" cy="62" r="56"/><circle cx="190" cy="82" r="52"/>
      <circle cx="100" cy="120" r="46"/><circle cx="165" cy="122" r="46"/>
      <circle cx="210" cy="170" r="9"/><circle cx="226" cy="196" r="6"/>
    </g>
    <g fill="none" stroke="var(--ink)" stroke-width="6" stroke-linejoin="round" stroke-linecap="round">
      <path d="M124 128 L90 96 C72 78 90 54 110 66 L122 76 L114 92 L126 104 L116 118 Z"/>
      <path d="M134 128 L168 96 C186 78 168 54 148 66 L134 78 L142 94 L130 106 L140 120 Z"/>
    </g>
  </svg>

  <svg class="bubble bubble-question" style="left:692px;top:540px" width="220" height="190" viewBox="0 0 220 190">
    <g fill="#ffffff">
      <circle cx="70" cy="70" r="46"/><circle cx="120" cy="52" r="48"/><circle cx="165" cy="78" r="44"/>
      <circle cx="95" cy="110" r="42"/><circle cx="150" cy="112" r="40"/>
      <circle cx="40" cy="150" r="8"/><circle cx="24" cy="176" r="6"/>
    </g>
    <text x="118" y="120" text-anchor="middle" font-family="Arimo, sans-serif" font-size="80" fill="var(--ink)">?</text>
  </svg>

  <h1 class="title">
    <span class="title-lead">Quiet</span>
    <span class="title-middle"><span class="white">Hands</span><span class="stack">On<br>Heavy</span></span>
    <span class="title-tail">Days:</span>
  </h1>
  <p class="subtitle">Standing beside someone across hard seasons</p>

  <div class="author">
    <p class="author-name">Daniel P. Hartwig</p>
    <p class="author-role">A GRIEF COUNSELOR</p>
  </div>
</main>
</body>
</html>
```